"Copper Meadow" red wine label design

We are a Sydney based company. We need to design a wine label for a Australian red wine.
Front label include following info:
Our brand: "Copper Meadow";
Product name: "Shiraz 2016";
In the bottom with small font: "Wine of Australia", "750ml"
Back label:
the back label would need to be consistent with the front label, with space for one paragraph of tasting notes, and ingredient info etc.
we would like to use white, gold and blue in this label. It should make customer feel the magical and beautiful moment of starry night.

We also need a logo design for the wine brand: "Copper Meadow"

I have attached a few wine bottle that used blue to give you some inspirations.

We need the design in AI file format.

Target Market(s)

both men and women

Industry/Entity Type

It Company

Logo Text

Copper Meadow

Requirements
Nice to have
• gold borderline, words; use of blue and white

```html
<!DOCTYPE html>
<html lang="en">
<head>
<meta charset="UTF-8">
<title>Copper Meadow Shiraz 2016 – Label Set</title>
<link rel="stylesheet" href="https://fonts.googleapis.com/css2?family=Gilda+Display&family=Crimson+Text:wght@600&family=Quicksand:wght@500&display=swap">
<style>
  :root {
    --backdrop: #d3cbc3;
    --paper: #ffffff;
    --ink: #1d1b28;
    --copper: #b5803f;
    --rule: #d9b98c;
    --night-deep: #221d46;
    --night-violet: #5b4592;
    --night-blue: #3a3f86;
    --night-glow: #8a68b0;
  }
  * { margin: 0; padding: 0; box-sizing: border-box; }
  html, body {
    width: 1200px;
    height: 900px;
    overflow: hidden;
    background: var(--backdrop);
  }
  .label-set {
    position: relative;
    width: 1200px;
    height: 900px;
  }
  .label {
    position: absolute;
    top: 150px;
    height: 600px;
    background: var(--paper);
    color: var(--ink);
    overflow: hidden;
  }
  .label--front { left: 110px; width: 504px; }
  .label--back  { left: 714px; width: 376px; }

  .brand-name {
    position: absolute;
    left: 0; right: 0;
    text-align: center;
    font-family: "Gilda Display", serif;
    font-size: 38px;
    letter-spacing: 1px;
    color: var(--ink);
  }
  .label--front .brand-name { top: 68px; }
  .label--back .brand-name { top: 52px; font-size: 36px; }

  .night-sky {
    position: absolute;
    left: 0;
    width: 100%;
    background:
      radial-gradient(ellipse 45% 60% at 65% 45%, var(--night-glow) 0%, transparent 70%),
      radial-gradient(ellipse 40% 70% at 20% 50%, var(--night-blue) 0%, transparent 75%),
      linear-gradient(100deg, var(--night-deep) 0%, var(--night-violet) 45%, var(--night-deep) 100%);
  }
  .label--front .night-sky { top: 150px; height: 232px; }
  .label--back .night-sky { top: 470px; height: 130px; }

  .product {
    position: absolute;
    top: 421px;
    left: 128px;
    width: 250px;
    border-top: 2px solid var(--rule);
    border-bottom: 2px solid var(--rule);
    height: 54px;
    display: flex;
    align-items: center;
    justify-content: center;
    font-family: "Gilda Display", serif;
    font-size: 38px;
    letter-spacing: 3px;
    color: var(--ink);
  }
  .vintage {
    position: absolute;
    top: 482px;
    left: 0; right: 0;
    text-align: center;
    font-family: "Gilda Display", serif;
    font-size: 30px;
    color: var(--ink);
  }

  .fine-print {
    position: absolute;
    font-family: "Quicksand", sans-serif;
    font-size: 17px;
    color: var(--copper);
    letter-spacing: 0.3px;
  }
  .label--front .fine-print { top: 565px; }
  .label--front .origin { left: 20px; }
  .label--front .volume { right: 20px; }
  .label--back .fine-print { top: 432px; }
  .label--back .abv { left: 34px; }
  .label--back .volume { right: 34px; }

  .tasting-notes {
    position: absolute;
    top: 140px;
    left: 36px;
    right: 36px;
    text-align: center;
    font-family: "Crimson Text", serif;
    font-weight: 600;
    font-size: 21px;
    line-height: 27.5px;
    color: var(--ink);
  }
  .accent-mark {
    position: absolute;
    top: 328px;
    left: 50%;
    width: 24px;
    height: 24px;
    margin-left: -12px;
    border-radius: 50%;
    background: radial-gradient(circle, var(--copper) 0%, rgba(181,128,63,0.15) 70%, transparent 72%);
  }
</style>
</head>
<body>
  <main class="label-set">
    <section class="label label--front" aria-label="Front label">
      <h1 class="brand-name">Copper Meadow</h1>
      <div class="night-sky" role="img" aria-label="Watercolour starry night sky with a crescent moon, a bare tree and a kangaroo silhouetted on the horizon"></div>
      <h2 class="product">SHIRAZ</h2>
      <p class="vintage">2016</p>
      <p class="fine-print origin">Wine of Australia</p>
      <p class="fine-print volume">750ml</p>
    </section>

    <section class="label label--back" aria-label="Back label">
      <h2 class="brand-name">Copper Meadow</h2>
      <p class="tasting-notes">Lorem ipsum dolor sit amet, consectetuer adip&shy;iscing elit, sed diam nonummy nibh euismod tincidunt ut laoreet dolore magna aliquam</p>
      <span class="accent-mark" role="img" aria-label="Small gold star accent"></span>
      <p class="fine-print abv">Alc 15.1%</p>
      <p class="fine-print volume">750ml</p>
      <div class="night-sky" role="img" aria-label="Watercolour starry night sky with a crescent moon"></div>
    </section>
  </main>
</body>
</html>
```